Metal Fabrication Business Cards

We need a business card for our business of Metal Fabrication/Welding. Our company is called "Hadley's Metal Fabrication"

We are a metal fabrication business which takes on "high class" clients- dealing with some of the biggest builders in Australia. Our work is neat, and the type of work we do is 2nd to none for quality. We want to show that on our cards. However, we would love to show a side that is down to earth and a bit more modern and contemporary - we are all young in business so would love to show that side - rather than a boring "very straight looking" card. We always have a clean workshop and take pride in our presentation. We want to come across like we are very rich, but would love to go for a surf as well! A card that basically says we have high class and will charge you a high rate - but the quality will be outstanding.

Front of card: - Simply but sharp!
-Thinking maybe white card - with nice black writing.
-On the right hand side of card a person welding - or holding a welder.
- My business name - Hadley's Metal Fabrication
-Also maybe my name - which is 'Corey" (if it doesn't work, we can put this on the back of card.)
- if needed to look better - we can put keywords on front of card like "metal fabrication, sheet metal, welding etc" but I dont want it to be crowded.

Back of card: - Also make smart but sharp!
Put details such as:
04387 21 914
hadley.fabrication@tinmailbox.com.au
7/32 Keel Street
East Marrobel QLD 4817
www.korvinfabrication.com.au
ABN 72 615 803 914

thats just an idea - its now up to you. I don't mind what you come up with - as long as it stands out from the rest and looks sharp, professional but contemporary.

Business

Put details such as:
04387 21 914
7/32 Keel Street
East Marrobel QLD 4817
ABN 72 615 803 914

Hadley's Metal Fabrication

```html
<!DOCTYPE html>
<html lang="en">
<head>
<meta charset="utf-8">
<title>Hadley's Metal Fabrication – Business Cards</title>
<link href="https://fonts.googleapis.com/css2?family=Open+Sans:wght@400;600;700;800&display=swap" rel="stylesheet">
<style>
  :root {
    --stage: #333333;
    --stage-edge: #262626;
    --card-white: #ffffff;
    --ink: #1a1a1a;
    --ink-soft: #4a4a4a;
    --steel-light: #f2f2f2;
    --steel-mid: #bfbfbf;
    --steel-dark: #6e6e6e;
    --rivet: #d9d9d9;
  }
  * { box-sizing: border-box; margin: 0; padding: 0; }
  html, body { width: 900px; height: 1200px; overflow: hidden; }
  body {
    background: radial-gradient(ellipse at center, var(--stage) 0%, var(--stage-edge) 100%);
    font-family: "Open Sans", Arial, sans-serif;
    color: var(--ink);
    position: relative;
  }
  .card {
    position: absolute;
    left: 66px;
    width: 768px;
    box-shadow: 0 14px 30px rgba(0,0,0,.55);
    overflow: hidden;
  }
  .card-front { top: 120px; height: 435px; background: var(--card-white); }
  .card-back { top: 615px; height: 480px; }

  .steel-band {
    position: absolute; left: 0; width: 100%; height: 56px;
    background: linear-gradient(90deg, var(--steel-dark) 0%, var(--steel-light) 22%, var(--steel-mid) 45%, var(--steel-light) 70%, var(--steel-dark) 100%);
  }
  .steel-band::after {
    content: ""; position: absolute; inset: 0;
    background: linear-gradient(180deg, rgba(255,255,255,.35) 0%, rgba(0,0,0,.15) 60%, rgba(0,0,0,.35) 100%);
  }
  .steel-band-top { top: 0; border-bottom: 2px solid #555; }
  .steel-band-bottom { bottom: 0; border-top: 2px solid #555; }
  .rivets {
    position: absolute; left: 24px; right: 24px; top: 50%;
    transform: translateY(-50%);
    display: flex; justify-content: space-between; z-index: 1;
  }
  .rivet {
    width: 10px; height: 10px; border-radius: 50%;
    background: radial-gradient(circle at 35% 35%, #fff 0%, var(--rivet) 45%, #777 100%);
    box-shadow: 0 1px 1px rgba(0,0,0,.5);
  }

  .brand { display: flex; flex-direction: column; align-items: center; text-align: center; }
  .brand-dot {
    width: 96px; height: 96px; border-radius: 50%;
    border: 6px solid var(--ink);
    margin-bottom: 16px;
  }
  .brand-name {
    font-weight: 800; font-size: 26px; letter-spacing: 3px;
    text-transform: uppercase; line-height: 1.25; color: var(--ink);
  }

  .card-front .brand { position: absolute; left: 40px; top: 96px; width: 350px; }
  .divider {
    position: absolute; left: 430px; top: 110px; width: 2px; height: 215px;
    background: var(--ink);
  }
  .contact { position: absolute; left: 456px; top: 104px; width: 300px; }
  .contact-name { font-weight: 700; font-size: 24px; letter-spacing: 1px; text-transform: uppercase; }
  .contact-role { font-size: 14px; color: var(--ink-soft); margin-bottom: 14px; }
  .contact-address { font-size: 14px; line-height: 1.4; margin-bottom: 16px; }
  .contact-list { list-style: none; }
  .contact-list li {
    display: flex; align-items: center; gap: 10px;
    font-size: 14px; line-height: 1; margin-bottom: 10px; white-space: nowrap;
  }
  .contact-icon { width: 18px; height: 18px; flex: none; }

  .card-back {
    background:
      linear-gradient(125deg, rgba(255,255,255,0) 0%, rgba(255,255,255,.55) 30%, rgba(255,255,255,0) 48%, rgba(255,255,255,.45) 70%, rgba(255,255,255,0) 100%),
      linear-gradient(180deg, #e8e8e8 0%, #bdbdbd 55%, #d6d6d6 100%);
  }
  .card-back .brand { position: absolute; left: 0; right: 0; top: 82px; }
  .card-back .brand-name { font-size: 34px; letter-spacing: 5px; }
  .services {
    position: absolute; left: 0; right: 0; top: 410px;
    text-align: center; font-weight: 700; font-size: 15px; letter-spacing: 4px;
    text-transform: uppercase; color: var(--ink);
  }
  .services span { margin: 0 10px; }
</style>
</head>
<body>

<section class="card card-front" aria-label="Business card front">
  <div class="steel-band steel-band-top">
    <div class="rivets"><i class="rivet"></i><i class="rivet"></i><i class="rivet"></i><i class="rivet"></i><i class="rivet"></i><i class="rivet"></i><i class="rivet"></i><i class="rivet"></i><i class="rivet"></i><i class="rivet"></i></div>
  </div>

  <div class="brand">
    <div class="brand-dot"></div>
    <p class="brand-name">Hadley's<br>Metal Fabrication</p>
  </div>

  <div class="divider"></div>

  <div class="contact">
    <p class="contact-name">Corey</p>
    <p class="contact-role">Managing Director</p>
    <p class="contact-address">7/32 Keel Street<br>East Marrobel QLD 4817</p>
    <ul class="contact-list">
      <li>
        <svg class="contact-icon" viewBox="0 0 18 18"><rect width="18" height="18" rx="3" fill="#1a1a1a"/><path d="M5.5 4h2l1 3-1.3 1a7 7 0 0 0 2.8 2.8l1-1.3 3 1v2c0 .6-.5 1-1 1A9 9 0 0 1 4.5 5c0-.5.4-1 1-1z" fill="#fff"/></svg>
        04387 21 914
      </li>
      <li>
        <svg class="contact-icon" viewBox="0 0 18 18"><rect width="18" height="18" rx="3" fill="#1a1a1a"/><rect x="4" y="5.5" width="10" height="7" fill="none" stroke="#fff" stroke-width="1.2"/><path d="M4 5.5l5 4 5-4" fill="none" stroke="#fff" stroke-width="1.2"/></svg>
        hadley.fabrication@tinmailbox.com.au
      </li>
      <li>
        <svg class="contact-icon" viewBox="0 0 18 18"><rect width="18" height="18" rx="3" fill="#1a1a1a"/><circle cx="9" cy="9" r="5" fill="none" stroke="#fff" stroke-width="1.2"/><ellipse cx="9" cy="9" rx="2.2" ry="5" fill="none" stroke="#fff" stroke-width="1"/><path d="M4 9h10" stroke="#fff" stroke-width="1"/></svg>
        www.korvinfabrication.com.au
      </li>
      <li>
        <svg class="contact-icon" viewBox="0 0 18 18"><rect width="18" height="18" rx="3" fill="#1a1a1a"/><rect x="4.5" y="4" width="9" height="10" fill="none" stroke="#fff" stroke-width="1.2"/><path d="M6.5 7h5M6.5 9h5M6.5 11h3" stroke="#fff" stroke-width="1"/></svg>
        ABN 72 615 803 914
      </li>
    </ul>
  </div>

  <div class="steel-band steel-band-bottom">
    <div class="rivets"><i class="rivet"></i><i class="rivet"></i><i class="rivet"></i><i class="rivet"></i><i class="rivet"></i><i class="rivet"></i><i class="rivet"></i><i class="rivet"></i><i class="rivet"></i><i class="rivet"></i></div>
  </div>
</section>

<section class="card card-back" role="img" aria-label="Business card back on brushed steel finish">
  <div class="brand">
    <div class="brand-dot"></div>
    <p class="brand-name">Hadley's<br>Metal Fabrication</p>
  </div>
  <p class="services">Metal Fabrication<span>|</span>Sheet Metal<span>|</span>Welding<span>|</span>Etc</p>
</section>

</body>
</html>
```